Holiday Sale 2026 Graphics for New Year

I want to create 10 social media graphics (new Instagram size 4:5 (1080 x 1350 pixels) focusing on our Holiday Sale Graphics, using any of the pics attached. Use the attached pics, NO RANDOM STOCK PHOTOGRAPHY. For the color scheme of the graphics, they should all be complementary to the product colors in the photos.
You can add any of the photos attached but none are required. You can do some of the graphics in all text. I mainly need BOLD text that says one of the headlines with the pics (10 total):
1. 25% OFF Holiday Sale: New You Starts Now!
2. 25% OFF Everything: New Year, New You
3. 25% OFF Christmas Sale 🎁 Feel Amazing Again!
4. Holiday Treat: 25% OFF Your Favorites
5. 25% OFF All Supplements ✨ New Year Reset!
6. Holiday Magic: 25% OFF Every Supplement
7. 25% OFF to Kickstart Your New Year Goals
8. New Year, New Waistline! 25% OFF Sale
9. Holiday Sale: 25% OFF Everything
10. A Better You Begins With 25% OFF

```html
<!DOCTYPE html>
<html lang="en">
<head>
<meta charset="utf-8">
<title>Holiday Sale Social Graphics</title>
<link href="https://fonts.googleapis.com/css2?family=Oswald:wght@600;700&display=swap" rel="stylesheet">
<style>
  :root {
    --board: #808080;
    --card: #ffffff;
    --purple: #3a2a6e;
    --red: #c7212f;
    --green: #1f4b3b;
    --blue: #2359a9;
    --magenta: #9a2f6a;
    --plum: #4a2137;
    --bottle-light: #eef0f2;
    --bottle-mid: #c9ced6;
  }
  html, body {
    margin: 0;
    width: 1200px;
    height: 2446px;
    overflow: hidden;
    background: var(--board);
  }
  .sheet {
    position: relative;
    width: 1200px;
    height: 2446px;
  }
  .post {
    position: absolute;
    width: 323px;
    height: 404px;
    background:
      radial-gradient(circle at 25% 20%, rgba(0,0,0,0.035), transparent 45%),
      radial-gradient(circle at 80% 75%, rgba(0,0,0,0.03), transparent 45%),
      var(--card);
    overflow: hidden;
    font-family: "Oswald", "Arial Narrow", sans-serif;
    font-weight: 700;
    color: var(--ink);
  }
  .post__frame {
    position: absolute;
    left: 20px; right: 20px; top: 24px; bottom: 24px;
    border: 1.5px solid var(--ink);
    border-radius: 4px;
  }
  .post__headline {
    position: absolute;
    left: 0; right: 0;
    text-align: center;
    text-transform: uppercase;
    white-space: nowrap;
    letter-spacing: -0.5px;
  }
  .post__headline span { display: block; line-height: 1.08; }
  .product-shot {
    position: absolute;
    border-radius: 6px;
    background: linear-gradient(90deg, var(--bottle-mid), var(--bottle-light) 30%, var(--bottle-mid) 55%, var(--bottle-light) 80%, var(--bottle-mid));
  }
  .col-left { left: 263px; }
  .col-right { left: 597px; }
  .row-1 { top: 164px; }
  .row-2 { top: 578px; }
  .row-3 { top: 994px; }
  .row-4 { top: 1409px; }
  .row-5 { top: 1824px; }
  .ink-purple { --ink: var(--purple); }
  .ink-red { --ink: var(--red); }
  .ink-green { --ink: var(--green); }
  .ink-blue { --ink: var(--blue); }
  .ink-magenta { --ink: var(--magenta); }
  .ink-plum { --ink: var(--plum); }
</style>
</head>
<body>
<main class="sheet">

  <section class="post col-left row-1 ink-purple">
    <div class="post__frame"></div>
    <h2 class="post__headline" style="top:38px;margin:0">
      <span style="font-size:66px">25% OFF</span>
      <span style="font-size:41px">Holiday Sale</span>
      <span style="font-size:68px">New You</span>
      <span style="font-size:46px">Starts Now!</span>
    </h2>
    <div class="product-shot" style="left:63px;top:287px;width:201px;height:112px" role="img" aria-label="Four supplement bottles"></div>
  </section>

  <section class="post col-right row-1 ink-red">
    <div class="post__frame"></div>
    <h2 class="post__headline" style="top:72px;margin:0">
      <span style="font-size:66px">25% OFF</span>
      <span style="font-size:47px">Everything</span>
      <span style="font-size:60px">New Year</span>
      <span style="font-size:66px">New You</span>
    </h2>
  </section>

  <section class="post col-left row-2 ink-green">
    <div class="post__frame"></div>
    <h2 class="post__headline" style="top:44px;margin:0">
      <span style="font-size:64px">25% OFF</span>
      <span style="font-size:38px">Christmas Sale</span>
      <span style="font-size:42px">Feel Amazing</span>
      <span style="font-size:82px;line-height:1">Again!</span>
    </h2>
    <div class="product-shot" style="left:43px;top:286px;width:237px;height:107px" role="img" aria-label="Supplement bottles lying in soft fabric"></div>
  </section>

  <section class="post col-right row-2 ink-blue">
    <div class="post__frame"></div>
    <h2 class="post__headline" style="top:58px;margin:0">
      <span style="font-size:38px">Holiday Treat</span>
      <span style="font-size:66px">25% OFF</span>
      <span style="font-size:100px;line-height:1">Your</span>
      <span style="font-size:52px">Favorites</span>
    </h2>
  </section>

  <section class="post col-left row-3 ink-magenta">
    <div class="post__frame"></div>
    <h2 class="post__headline" style="top:68px;margin:0">
      <span style="font-size:62px">25% OFF</span>
      <span style="font-size:35px">All Supplements</span>
      <span style="font-size:58px">New Year</span>
      <span style="font-size:82px;line-height:1">Reset!</span>
    </h2>
  </section>

  <section class="post col-right row-3 ink-plum">
    <div class="post__frame"></div>
    <div class="product-shot" style="left:53px;top:8px;width:253px;height:88px" role="img" aria-label="Four supplement bottles in a row"></div>
    <h2 class="post__headline" style="top:100px;margin:0">
      <span style="font-size:62px">25% OFF</span>
      <span style="font-size:33px">Every Supplement</span>
      <span style="font-size:68px">Holiday</span>
      <span style="font-size:80px;line-height:1">Magic</span>
    </h2>
  </section>

  <section class="post col-left row-4 ink-red">
    <div class="post__frame"></div>
    <h2 class="post__headline" style="top:72px;margin:0">
      <span style="font-size:64px">25% OFF</span>
      <span style="font-size:40px">To Kickstart</span>
      <span style="font-size:37px">Your New Year</span>
      <span style="font-size:86px;line-height:1">Goals</span>
    </h2>
  </section>

  <section class="post col-right row-4 ink-purple">
    <div class="post__frame"></div>
    <h2 class="post__headline" style="top:50px;margin:0">
      <span style="font-size:64px">25% OFF</span>
      <span style="font-size:110px;line-height:0.98">Sale</span>
      <span style="font-size:55px">New Year,</span>
      <span style="font-size:37px">New Waistline!</span>
    </h2>
  </section>

  <section class="post col-left row-5 ink-magenta">
    <div class="post__frame"></div>
    <h2 class="post__headline" style="top:46px;margin:0">
      <span style="font-size:64px">25% OFF</span>
      <span style="font-size:45px">Everything</span>
      <span style="font-size:68px">Holiday</span>
      <span style="font-size:116px;line-height:0.98">Sale</span>
    </h2>
  </section>

  <section class="post col-right row-5 ink-green">
    <div class="post__frame"></div>
    <h2 class="post__headline" style="top:56px;margin:0">
      <span style="font-size:60px">A Better</span>
      <span style="font-size:50px">You Begins</span>
      <span style="font-size:108px;line-height:0.98">With</span>
      <span style="font-size:62px">25% OFF</span>
    </h2>
  </section>

</main>
</body>
</html>
```